E-Commerce Website Update for Bamboo Poles Company

Existing website at:

http://www.reedcraftstudio.example/
http://www.reedcraftstudio.example/pages/product-and-price-list

Two pages to design: home page and "price list" page.

Info for home page as follows:

HOME PAGE:

Header:
Company Name: reedcraft studio
Telephone: 1 888 412 5093

Across the top:
Home | Price List | Blog | FAQ | About | Contact

Down the side:
About Bamboo
Wedding Arbors
Bamboo For Flutes
Black Bamboo
Spotted Bamboo
Bamboo Carpentry
Photo Gallery
All Products & Prices
Blog
FAQ
About
Contact

Should have shopping cart and search buttons on top.
Please see ai file, attached for logo (leaf) and font
In addition the homepage should have one or two sections for promotions

Chosen design will be asked to help deign a PRODUCT AND PRICE LIST page similar to the one we have now, but with "LEARN MORE" and "ORDER NOW" buttons for each item.
Updates

Reason: Thanks  for all the designs so far; giving an extra week for extra consideration.

Target Market(s)

Consumers, wedding planners.

Industry/Entity Type

Shopping

Requirements
Must have
• Clean, easy to read design.
Should not have
• No flash animation.

```html
<!DOCTYPE html>
<html lang="en">
<head>
<meta charset="utf-8">
<title>Product and Price List – reedcraft studio</title>
<link href="https://fonts.googleapis.com/css2?family=Arimo:wght@400;700&display=swap" rel="stylesheet">
<style>
:root{
  --green:#5a9a1e;
  --green-dark:#3f7d10;
  --green-light:#7cb83a;
  --cream:#efefd9;
  --cream-light:#f5f5e6;
  --cream-dark:#e7e7c6;
  --page:#f7f6f1;
  --line:#d8d8c0;
  --text:#333;
  --muted:#777;
  --white:#fff;
}
*{box-sizing:border-box;margin:0;padding:0}
html,body{width:943px;height:1200px;overflow:hidden}
body{font-family:"Arimo",Arial,sans-serif;color:var(--text);background:var(--page);position:relative}
a{color:inherit;text-decoration:none}

.top-strip{position:absolute;left:0;top:0;width:943px;height:8px;background:var(--green)}
.site-header{position:absolute;left:0;top:8px;width:943px;height:102px;background:var(--cream);border-bottom:1px solid var(--line)}
.brand{position:absolute;left:62px;top:22px;font-size:38px;line-height:36px;color:var(--green);font-weight:400;letter-spacing:-.5px}
.phone{position:absolute;left:396px;top:30px;display:flex;gap:12px;align-items:center}
.phone-label{font-size:12px;font-weight:700;color:#444;letter-spacing:.3px}
.phone-number{font-size:25px;color:var(--green);margin-top:4px}
.cart{position:absolute;left:745px;top:14px;width:160px}
.cart-title{position:absolute;left:50px;top:6px;font-size:12px;font-weight:700;color:#555;white-space:nowrap}
.cart-status{position:absolute;left:54px;top:30px;font-size:11px;color:#666;white-space:nowrap}
.cart svg{position:absolute;left:0;top:8px}
.cart-buttons{position:absolute;left:13px;top:58px;display:flex;gap:7px}
.btn{font-size:11px;padding:4px 9px;border-radius:3px;white-space:nowrap}
.btn-green{background:var(--green);color:var(--white)}
.btn-white{background:var(--white);color:#333;border:1px solid #bbb}

.main-nav{position:absolute;left:43px;top:107px;width:857px;height:32px;background:linear-gradient(var(--green-light),var(--green));border-radius:3px;display:flex;align-items:center;padding-left:16px}
.main-nav a{color:var(--white);font-size:12px;margin-right:40px;text-transform:uppercase;letter-spacing:.5px}
.main-nav a.active{background:var(--green-dark);padding:3px 10px;border-radius:2px;margin-right:40px}
.search{position:absolute;right:10px;top:5px;display:flex;gap:4px}
.search input{width:165px;height:22px;border:0;border-radius:2px;background:var(--white)}
.search button{height:22px;padding:0 7px;border:0;border-radius:2px;background:var(--green-dark);color:var(--white);font:12px "Arimo",Arial,sans-serif}

.sidebar{position:absolute;left:43px;top:167px;width:221px;height:700px;background:var(--cream-light);border:1px solid var(--line)}
.side-head{height:28px;background:linear-gradient(var(--green-light),var(--green));color:var(--white);font-size:13px;font-weight:700;display:flex;align-items:center;justify-content:space-between;padding:0 12px 0 14px;text-transform:uppercase}
.side-head .dot{width:18px;height:18px;border-radius:50%;background:var(--white);display:flex;align-items:center;justify-content:center}
.categories{list-style:none;padding:9px 6px 6px}
.categories li{height:26px;display:flex;align-items:center;justify-content:space-between;padding:0 10px 0 7px;font-size:11.5px;text-transform:uppercase;border-bottom:1px solid var(--line);color:#333}
.categories li.current{background:var(--green);color:var(--white)}
.chev{font-size:14px;color:var(--green)}
.current .chev{color:var(--white)}
.offer-title{font-size:11.5px;text-align:center;margin:14px 0 10px;letter-spacing:.3px}
.offer-photo{width:158px;height:121px;margin:0 auto;background:linear-gradient(135deg,#c9b48a,#8d6e43 60%,#d6c7a3);border:3px solid var(--white);box-shadow:0 0 2px #aaa}
.price-old{margin:12px 0 0 32px;font-size:12px;color:#999;text-decoration:line-through}
.price-row{display:flex;justify-content:space-between;align-items:baseline;padding:0 28px 0 32px}
.price-new{font-size:21px;font-weight:700;color:var(--green)}
.more{font-size:11px;text-decoration:underline;color:#555}
.follow{position:absolute;left:0;bottom:0;width:219px;height:94px;background:var(--cream-dark);padding:12px 14px}
.follow h3{font-size:13px;color:var(--green);font-weight:700;letter-spacing:.4px}
.follow-icons{display:flex;gap:12px;justify-content:center;margin-top:14px}
.follow-icons span{width:31px;height:31px;border-radius:4px;background:var(--green)}

.content{position:absolute;left:266px;top:167px;width:634px;height:969px;background:var(--white);box-shadow:0 0 4px rgba(0,0,0,.2);padding:0 15px}
.content h1{font-size:17px;font-weight:400;letter-spacing:.6px;margin:16px 0 0 18px;padding-bottom:9px;border-bottom:1px solid #ddd;text-transform:uppercase;color:#111}
.jump{font-size:11px;color:#555;margin:8px 0 0 18px}
.jump a{color:var(--green);text-decoration:underline}
.product-group{margin-top:20px;border:1px solid var(--line);border-top:0}
.group-head{height:28px;background:linear-gradient(var(--green-light),var(--green));color:var(--white);font-size:13px;font-weight:700;display:flex;align-items:center;justify-content:space-between;padding:0 14px 0 8px;text-transform:uppercase}
.group-head a{font-size:10px;text-transform:lowercase}
table{width:100%;border-collapse:collapse;font-size:11px;color:#666}
th{background:var(--cream-light);height:23px;font-weight:700;color:#555;letter-spacing:.6px;border-right:1px solid var(--line);border-bottom:1px solid var(--line)}
td{height:78px;text-align:center;border-right:1px solid var(--line);border-bottom:1px solid var(--line)}
th:last-child,td:last-child{border-right:0}
tr:last-child td{border-bottom:0}
.thumb{width:76px;height:64px;margin:0 auto;background:linear-gradient(90deg,#bcbcb4,#c9b27a 30%,#a38c55 55%,#cbb789 80%,#bdbdb5)}

.site-footer{position:absolute;left:0;top:1139px;width:943px;height:61px;background:var(--green);color:var(--white);font-size:11px}
.footer-links{position:absolute;left:50px;top:9px}
.footer-links a{margin-right:4px}
.copyright{position:absolute;left:48px;top:30px;letter-spacing:.2px}
.footer-brand{position:absolute;right:42px;top:10px;font-size:19px;line-height:17px;text-align:left}
</style>
</head>
<body>
<div class="top-strip"></div>
<header class="site-header">
  <div class="brand">reedcraft<br>studio</div>
  <div class="phone">
    <svg width="52" height="42" viewBox="0 0 52 42" aria-hidden="true">
      <path d="M4 12 Q26 -2 48 12 L46 18 L36 16 L35 11 Q26 8 17 11 L16 16 L6 18 Z" fill="#222"/>
      <path d="M14 20 L38 20 L46 38 L6 38 Z" fill="#333"/>
      <circle cx="26" cy="29" r="6" fill="#777"/>
    </svg>
    <div>
      <div class="phone-label">ORDER TOLL-FREE 24/7</div>
      <div class="phone-number">1 888 412 5093</div>
    </div>
  </div>
  <div class="cart">
    <svg width="46" height="40" viewBox="0 0 46 40" aria-hidden="true">
      <path d="M2 6 L8 6 L12 30 L38 30" fill="none" stroke="#b07a10" stroke-width="3"/>
      <path d="M9 10 L44 10 L39 26 L12 26 Z" fill="#f0b31b"/>
      <circle cx="15" cy="35" r="3" fill="#8a5c08"/><circle cx="34" cy="35" r="3" fill="#8a5c08"/>
    </svg>
    <div class="cart-title">My Shopping Cart</div>
    <div class="cart-status">Item: 0 Total: $0.00</div>
    <div class="cart-buttons"><a class="btn btn-green" href="#">View Cart</a><a class="btn btn-white" href="#">Checkout</a></div>
  </div>
</header>

<nav class="main-nav">
  <a class="active" href="#">Home</a><a href="#">Price List</a><a href="#">Blog</a><a href="#">FAQ</a><a href="#">About</a><a href="#">Contact</a>
  <form class="search"><input type="text" aria-label="Search"><button type="button">SEARCH</button></form>
</nav>

<aside class="sidebar">
  <div class="side-head">Categories<span class="dot"><svg width="10" height="10" viewBox="0 0 10 10"><path d="M3 1 L7 5 L3 9" fill="none" stroke="#5a9a1e" stroke-width="2"/></svg></span></div>
  <ul class="categories">
    <li>About Bamboo<span class="chev">›</span></li>
    <li class="current">Wedding Arbors<span class="chev">›</span></li>
    <li>Bamboo for Flutes<span class="chev">›</span></li>
    <li>Black Bamboo<span class="chev">›</span></li>
    <li>Spotted Bamboo<span class="chev">›</span></li>
    <li>Bamboo Carpentry<span class="chev">›</span></li>
    <li>Photo Gallery<span class="chev">›</span></li>
    <li>All Products &amp; Prices<span class="chev">›</span></li>
    <li>Blog<span class="chev">›</span></li>
    <li>FAQ<span class="chev">›</span></li>
    <li>About<span class="chev">›</span></li>
    <li>Contact<span class="chev">›</span></li>
  </ul>
  <div class="side-head">Special Offer<span class="dot"><svg width="10" height="10" viewBox="0 0 10 10"><path d="M3 1 L7 5 L3 9" fill="none" stroke="#5a9a1e" stroke-width="2"/></svg></span></div>
  <p class="offer-title">4 PCS 2" X 8' NAN BAMBOO POLES</p>
  <div class="offer-photo" role="img" aria-label="Stack of cut bamboo poles seen from their ends"></div>
  <p class="price-old">$34.00</p>
  <div class="price-row"><span class="price-new">$24.00</span><a class="more" href="#">More Detailes</a></div>
  <div class="follow">
    <h3>FOLLOW US ON:</h3>
    <div class="follow-icons"><span></span><span></span><span></span></div>
  </div>
</aside>

<main class="content">
  <h1>Product and Price List</h1>
  <p class="jump">Jump to: <a href="#">Black Poles</a>, <a href="#">Spotted Poles</a>, <a href="#">Bamboo Wedding Arbors</a></p>

  <section class="product-group">
    <div class="group-head">Bamboo Poles<a href="#">see all</a></div>
    <table>
      <colgroup><col style="width:92px"><col style="width:37px"><col style="width:108px"><col style="width:104px"><col style="width:80px"><col style="width:62px"><col></colgroup>
      <tr><th>Click on photo</th><th>Item</th><th>Description</th><th>Dimensions</th><th>Pole Price</th><th>Packing</th><th>Carton Price</th></tr>
      <tr><td><div class="thumb" role="img" aria-label="Reed bamboo poles"></div></td><td>C1</td><td>Reed Bamboo</td><td>3/8"dia. × 60"</td><td>$0.53</td><td>15 poles</td><td>$8.00/carton</td></tr>
      <tr><td><div class="thumb" role="img" aria-label="Reed bamboo poles"></div></td><td>C1</td><td>Reed Bamboo</td><td>3/8"dia. × 60"</td><td>$0.53</td><td>15 poles</td><td>$8.00/carton</td></tr>
      <tr><td><div class="thumb" role="img" aria-label="Reed bamboo poles"></div></td><td>C1</td><td>Reed Bamboo</td><td>3/8"dia. × 60"</td><td>$0.53</td><td>15 poles</td><td>$8.00/carton</td></tr>
    </table>
  </section>

  <section class="product-group">
    <div class="group-head">Black Poles<a href="#">see all</a></div>
    <table>
      <colgroup><col style="width:92px"><col style="width:37px"><col style="width:108px"><col style="width:104px"><col style="width:80px"><col style="width:62px"><col></colgroup>
      <tr><th>Click on photo</th><th>Item</th><th>Description</th><th>Dimensions</th><th>Pole Price</th><th>Packing</th><th>Carton Price</th></tr>
      <tr><td><div class="thumb" role="img" aria-label="Reed bamboo poles"></div></td><td>C1</td><td>Reed Bamboo</td><td>3/8"dia. × 60"</td><td>$0.53</td><td>15 poles</td><td>$8.00/carton</td></tr>
      <tr><td><div class="thumb" role="img" aria-label="Reed bamboo poles"></div></td><td>C1</td><td>Reed Bamboo</td><td>3/8"dia. × 60"</td><td>$0.53</td><td>15 poles</td><td>$8.00/carton</td></tr>
      <tr><td><div class="thumb" role="img" aria-label="Reed bamboo poles"></div></td><td>C1</td><td>Reed Bamboo</td><td>3/8"dia. × 60"</td><td>$0.53</td><td>15 poles</td><td>$8.00/carton</td></tr>
    </table>
  </section>

  <section class="product-group">
    <div class="group-head">Spotted Poles</div>
    <table>
      <colgroup><col style="width:92px"><col style="width:37px"><col style="width:108px"><col style="width:104px"><col style="width:80px"><col style="width:62px"><col></colgroup>
      <tr><th>Click on photo</th><th>Item</th><th>Description</th><th>Dimensions</th><th>Pole Price</th><th>Packing</th><th>Carton Price</th></tr>
      <tr><td><div class="thumb" role="img" aria-label="Reed bamboo poles"></div></td><td>C1</td><td>Reed Bamboo</td><td>3/8"dia. × 60"</td><td>$0.53</td><td>15 poles</td><td>$8.00/carton</td></tr>
      <tr><td><div class="thumb" role="img" aria-label="Reed bamboo poles"></div></td><td>C1</td><td>Reed Bamboo</td><td>3/8"dia. × 60"</td><td>$0.53</td><td>15 poles</td><td>$8.00/carton</td></tr>
    </table>
  </section>
</main>

<footer class="site-footer">
  <div class="footer-links"><a href="#">Home</a> | <a href="#">Price List</a> | <a href="#">Blog</a> | <a href="#">FAQ</a> | <a href="#">About</a> | <a href="#">Contact</a></div>
  <div class="copyright">Copyright © 2011 reedcraft studio. All Rights Reserved. All prices USD.</div>
  <div class="footer-brand">reedcraft<br>studio</div>
</footer>
</body>
</html>
```